Social-Business Application (iOS)

App is very simillar to "Murmel" from AppHarbor

Please see the wireframes!

We need a design for application according to attached wireframes.
Social-Business application is a mobile app, that let's user to login, using ProNexa and browse through other users content (meme's). There are 2 home pages and 4 categories (displayed in wireframes). They are pretty simillar to each other. First one is called "Say Something" and the other one called "Ask Something". On "Say Something" page user is able to browse through meme's with pictures. There are several options to each meme, as well as reply to meme with your own meme.
"Ask Something" has only 2 differences.
1. There are always "?" in the end of each meme.
2. Only plain background with different colors are acceptable.
User is also able to create meme's to each home page and category.

There is no First or Last name display! Only following info should be displayed:
Location, Industry, Number of ProNexa contacts.

There is also a simple chat function, that provides the ability to chat with author of the meme. On the chat preview we will show the meme preview Instead of profile picture.

Please, ask your questions.
Updates

Please, send your examples.

Please check out "Murmel" application for better understanding of the functionality and overall idea

https://apps.harborstore-example.com/store/apps/details?id=qz.murmel

I will report to our admin, to change Designer Payment to Commited if we will have at least one screen example from you, guys.

Target Market(s)

regular users, business users.
Adult Audience, Professional Audience.

Industry/Entity Type

Business

Font styles to use
Other font styles liked:
• Helvetica Neue

Requirements
Must have
• Design must have all screens and elements that are displayed in attached photos (wireframes).
Flat style is required.
Following the iOS guidelines is required.
Nice to have
• Design example could show different ui colors for each of home pages ("Ask Something" and "Say Something") to easily indicate on what home page user is.
Should not have
• The design should not be overloaded and should not use serif fonts like Times New Roman.

```html
<!DOCTYPE html>
<html lang="en">
<head>
<meta charset="utf-8">
<title>Latest – Social Business App Screens</title>
<link rel="stylesheet" href="https://fonts.googleapis.com/css2?family=Roboto:wght@400;500;700&display=swap">
<style>
  :root {
    --stage-bg: #8761a5;
    --purple: #9a6cc2;
    --purple-meta: #a493b4;
    --teal: #6cc0ae;
    --teal-meta: #93aaa6;
    --blue: #7a86c8;
    --green: #93bb6f;
    --card-bg: #ffffff;
    --label: #7d7d7d;
    --content-bg: #e9e8ea;
    --bar-text: #555555;
  }
  * { box-sizing: border-box; margin: 0; padding: 0; }
  html, body { width: 1200px; height: 728px; overflow: hidden; background: var(--stage-bg); }
  body { font-family: "Roboto", "Helvetica Neue", Arial, sans-serif; }

  .stage {
    position: relative; width: 981px; height: 595px;
    transform: scale(1.2232); transform-origin: 0 0;
  }

  .phone {
    position: absolute; top: 28px; width: 298px; height: 531px;
    background: linear-gradient(180deg, #f7f7f8 0%, #ecebee 100%);
    box-shadow: 0 2px 6px rgba(40, 20, 60, .25);
    overflow: hidden;
  }
  .phone--purple { left: 66px; --accent: var(--purple); --meta: var(--purple-meta); }
  .phone--blue { left: 459px; --accent: var(--blue); --meta: #9b9fbf; }
  .phone--green { left: 537px; --accent: var(--green); --meta: #9ab08a; }
  .phone--teal { left: 607px; --accent: var(--teal); --meta: var(--teal-meta); }

  .app-header { background: var(--accent); height: 61px; color: #fff; position: relative; }
  .status-bar { height: 19px; font-size: 11.5px; display: flex; align-items: center; padding: 0 6px; position: relative; }
  .status-bar .signal { display: flex; gap: 1.5px; margin-right: 4px; }
  .status-bar .signal i { width: 5px; height: 5px; border-radius: 50%; background: #fff; display: block; }
  .status-bar .signal i.off { background: none; border: 1px solid #fff; }
  .status-bar .carrier { margin-right: 10px; }
  .status-bar .time { position: absolute; left: 0; right: 0; text-align: center; }
  .status-bar .battery { margin-left: auto; display: flex; align-items: center; gap: 4px; }
  .status-bar .battery b { width: 21px; height: 9px; border: 1px solid #fff; padding: 1px; display: block; }
  .status-bar .battery b::after { content: ""; display: block; height: 100%; background: #fff; }

  .nav-bar { height: 42px; display: flex; align-items: center; justify-content: space-between; padding: 0 13px; position: relative; }
  .nav-bar .title { position: absolute; left: 0; right: 0; text-align: center; font-weight: 700; font-size: 15px; }
  .nav-bar svg { width: 20px; height: 20px; position: relative; }

  .pager { height: 46px; display: flex; justify-content: center; align-items: center; gap: 3px;
    background: linear-gradient(90deg, #e6e5e8, #fbfbfc 40%, #fbfbfc 60%, #e6e5e8); }
  .pager i { width: 6px; height: 6px; border-radius: 50%; background: #fff; display: block; box-shadow: 0 0 1px rgba(0,0,0,.25); }
  .pager i.active { background: var(--accent); box-shadow: none; }

  .feed { display: grid; grid-template-columns: 140px 140px; column-gap: 9px; row-gap: 13px; padding: 0 4px 0 4px; }
  .post { background: var(--card-bg); height: 172px; box-shadow: 0 1px 2px rgba(0,0,0,.12); }
  .post .label { height: 25px; line-height: 27px; padding-left: 7px; font-size: 11.5px; color: var(--label); }
  .post .media { height: 123px; }
  .post .meta { height: 24px; display: flex; justify-content: center; align-items: center; gap: 9px; font-size: 10.5px; color: var(--meta); }
  .post .meta span { display: flex; align-items: center; gap: 2px; }
  .post .meta svg { width: 10px; height: 10px; fill: var(--meta); }

  .composer { position: absolute; left: 0; right: 0; bottom: 0; height: 41px; background: #fff;
    display: flex; align-items: center; padding-left: 13px; gap: 9px; font-size: 14px; color: var(--bar-text);
    box-shadow: 0 -1px 3px rgba(0,0,0,.06); }
  .composer svg { width: 22px; height: 22px; }

  .media--jelly { background: radial-gradient(circle at 45% 45%, #d44f6c 0 18%, transparent 30%), linear-gradient(160deg, #f4e9ee 0%, #9fc8c2 55%, #4d7d80 100%); }
  .media--nebula { background: radial-gradient(circle at 40% 45%, #1c2b4a 0 20%, transparent 45%), linear-gradient(135deg, #b0365c 0%, #4b6c8c 50%, #c4485a 100%); }
  .media--tulips { background: radial-gradient(circle at 50% 55%, #f2e9e4 0 3%, transparent 5%), linear-gradient(180deg, #a3162e 0%, #c8233c 50%, #8d1226 100%); }
  .media--night { background: linear-gradient(180deg, #3552c8 0%, #2a2f7a 40%, #c9a635 55%, #273579 70%, #8a7a3a 100%); }

  .phone--blue .media--jelly { background: linear-gradient(160deg, #fbe7f6, #c64ab9 55%, #7a5f91); }
  .phone--blue .media--tulips { background: linear-gradient(180deg, #9c1890, #c72fb6 50%, #801a7c); }
  .phone--green .media--jelly { background: linear-gradient(160deg, #e8f4ef, #3cc4b0 55%, #5a6b6c); }
  .phone--green .media--tulips { background: linear-gradient(180deg, #1e8e7a, #2bb79d 50%, #176d5f); }
</style>
</head>
<body>
<svg width="0" height="0" style="position:absolute" aria-hidden="true">
  <symbol id="icon-menu" viewBox="0 0 20 20"><circle cx="10" cy="10" r="8.6" fill="none" stroke="#fff" stroke-width="1.5"/><path d="M6 7h8M6 10h8M6 13h8" stroke="#fff" stroke-width="1.4"/></symbol>
  <symbol id="icon-compose" viewBox="0 0 20 20"><path d="M10 2H2v16h16v-8" fill="none" stroke="#fff" stroke-width="1.6"/><path d="M7 13l1-3 8-8 2 2-8 8z" fill="none" stroke="#fff" stroke-width="1.5"/></symbol>
  <symbol id="icon-clock" viewBox="0 0 10 10"><circle cx="5" cy="5" r="5"/><path d="M5 2.2V5h2.2" stroke="#fff" stroke-width="1" fill="none"/></symbol>
  <symbol id="icon-heart" viewBox="0 0 10 10"><path d="M5 9.4L1 5.3C-.4 3.8.3 1 2.6 1 3.7 1 4.5 1.8 5 2.6 5.5 1.8 6.3 1 7.4 1 9.7 1 10.4 3.8 9 5.3z"/></symbol>
  <symbol id="icon-bubble" viewBox="0 0 10 10"><path d="M5 .8C2.2.8 0 2.5 0 4.7c0 1.1.6 2.1 1.5 2.8L1 9.6l2.5-1.2c.5.1 1 .2 1.5.2 2.8 0 5-1.7 5-3.9S7.8.8 5 .8z"/></symbol>
  <symbol id="icon-say" viewBox="0 0 22 22"><path d="M1.5 2.5h19v13h-11l-5 4v-4h-3z" fill="none" stroke="#555" stroke-width="1.5" stroke-linejoin="round"/><path d="M6 7.5h10M6 10.5h7" stroke="#555" stroke-width="1.4"/></symbol>
</svg>

<main class="stage">

  <section class="phone phone--purple" aria-label="Latest feed, purple theme">
    <header class="app-header">
      <div class="status-bar"><span class="signal"><i></i><i></i><i></i><i class="off"></i><i class="off"></i></span><span class="carrier">Carrier</span><span class="time">4:21 PM</span><span class="battery">100% <b></b></span></div>
      <nav class="nav-bar"><svg><use href="#icon-menu"/></svg><span class="title">Latest</span><svg><use href="#icon-compose"/></svg></nav>
    </header>
    <div class="pager"><i class="active"></i><i></i><i></i><i></i></div>
    <div class="feed">
      <article class="post"><div class="label">Location</div><div class="media media--jelly" role="img" aria-label="Photo of pink jellyfish in pale water"></div><div class="meta"><span><svg><use href="#icon-clock"/></svg>5m</span><span><svg><use href="#icon-heart"/></svg>0</span><span><svg><use href="#icon-bubble"/></svg>31</span></div></article>
      <article class="post"><div class="label">Location, other info</div><div class="media media--nebula" role="img" aria-label="Photo of a colourful star nebula"></div><div class="meta"><span><svg><use href="#icon-clock"/></svg>5m</span><span><svg><use href="#icon-heart"/></svg>0</span><span><svg><use href="#icon-bubble"/></svg>31</span></div></article>
      <article class="post"><div class="label">Location</div><div class="media media--tulips" role="img" aria-label="Photo of a red tulip field with one white tulip"></div><div class="meta"><span><svg><use href="#icon-clock"/></svg>5m</span><span><svg><use href="#icon-heart"/></svg>0</span><span><svg><use href="#icon-bubble"/></svg>31</span></div></article>
      <article class="post"><div class="label">Location, other info</div><div class="media media--night" role="img" aria-label="Painting of a night river with glowing reflections"></div><div class="meta"><span><svg><use href="#icon-clock"/></svg>5m</span><span><svg><use href="#icon-heart"/></svg>0</span><span><svg><use href="#icon-bubble"/></svg>31</span></div></article>
    </div>
    <footer class="composer"><svg><use href="#icon-say"/></svg>Say something</footer>
  </section>

  <section class="phone phone--blue" aria-label="Latest feed, blue theme">
    <header class="app-header">
      <div class="status-bar"><span class="signal"><i></i><i></i><i></i><i class="off"></i><i class="off"></i></span><span class="carrier">Carrier</span><span class="time">4:21 PM</span><span class="battery">100% <b></b></span></div>
      <nav class="nav-bar"><svg><use href="#icon-menu"/></svg><span class="title">Latest</span><svg><use href="#icon-compose"/></svg></nav>
    </header>
    <div class="pager"><i class="active"></i><i></i><i></i><i></i></div>
    <div class="feed">
      <article class="post"><div class="label">Location</div><div class="media media--jelly" role="img" aria-label="Photo of magenta-tinted jellyfish"></div><div class="meta"><span><svg><use href="#icon-clock"/></svg>5m</span><span><svg><use href="#icon-heart"/></svg>0</span><span><svg><use href="#icon-bubble"/></svg>31</span></div></article>
      <article class="post"><div class="label">Location, other info</div><div class="media media--nebula" role="img" aria-label="Photo of a star nebula"></div><div class="meta"><span><svg><use href="#icon-clock"/></svg>5m</span><span><svg><use href="#icon-heart"/></svg>0</span><span><svg><use href="#icon-bubble"/></svg>31</span></div></article>
      <article class="post"><div class="label">Location</div><div class="media media--tulips" role="img" aria-label="Photo of a magenta-tinted tulip field"></div><div class="meta"><span><svg><use href="#icon-clock"/></svg>5m</span><span><svg><use href="#icon-heart"/></svg>0</span><span><svg><use href="#icon-bubble"/></svg>31</span></div></article>
      <article class="post"><div class="label">Location, other info</div><div class="media media--night" role="img" aria-label="Painting of a night river"></div><div class="meta"><span><svg><use href="#icon-clock"/></svg>5m</span><span><svg><use href="#icon-heart"/></svg>0</span><span><svg><use href="#icon-bubble"/></svg>31</span></div></article>
    </div>
    <footer class="composer"><svg><use href="#icon-say"/></svg>Say something</footer>
  </section>

  <section class="phone phone--green" aria-label="Latest feed, green theme">
    <header class="app-header">
      <div class="status-bar"><span class="signal"><i></i><i></i><i></i><i class="off"></i><i class="off"></i></span><span class="carrier">Carrier</span><span class="time">4:21 PM</span><span class="battery">100% <b></b></span></div>
      <nav class="nav-bar"><svg><use href="#icon-menu"/></svg><span class="title">Latest</span><svg><use href="#icon-compose"/></svg></nav>
    </header>
    <div class="pager"><i class="active"></i><i></i><i></i><i></i></div>
    <div class="feed">
      <article class="post"><div class="label">Location</div><div class="media media--jelly" role="img" aria-label="Photo of teal-tinted jellyfish"></div><div class="meta"><span><svg><use href="#icon-clock"/></svg>5m</span><span><svg><use href="#icon-heart"/></svg>0</span><span><svg><use href="#icon-bubble"/></svg>31</span></div></article>
      <article class="post"><div class="label">Location, other info</div><div class="media media--nebula" role="img" aria-label="Photo of a star nebula"></div><div class="meta"><span><svg><use href="#icon-clock"/></svg>5m</span><span><svg><use href="#icon-heart"/></svg>0</span><span><svg><use href="#icon-bubble"/></svg>31</span></div></article>
      <article class="post"><div class="label">Location</div><div class="media media--tulips" role="img" aria-label="Photo of a teal-tinted tulip field"></div><div class="meta"><span><svg><use href="#icon-clock"/></svg>5m</span><span><svg><use href="#icon-heart"/></svg>0</span><span><svg><use href="#icon-bubble"/></svg>31</span></div></article>
      <article class="post"><div class="label">Location, other info</div><div class="media media--night" role="img" aria-label="Painting of a night river"></div><div class="meta"><span><svg><use href="#icon-clock"/></svg>5m</span><span><svg><use href="#icon-heart"/></svg>0</span><span><svg><use href="#icon-bubble"/></svg>31</span></div></article>
    </div>
    <footer class="composer"><svg><use href="#icon-say"/></svg>Say something</footer>
  </section>

  <section class="phone phone--teal" aria-label="Latest feed, teal theme">
    <header class="app-header">
      <div class="status-bar"><span class="signal"><i></i><i></i><i></i><i class="off"></i><i class="off"></i></span><span class="carrier">Carrier</span><span class="time">4:21 PM</span><span class="battery">100% <b></b></span></div>
      <nav class="nav-bar"><svg><use href="#icon-menu"/></svg><span class="title">Latest</span><svg><use href="#icon-compose"/></svg></nav>
    </header>
    <div class="pager"><i class="active"></i><i></i><i></i><i></i></div>
    <div class="feed">
      <article class="post"><div class="label">Location</div><div class="media media--jelly" role="img" aria-label="Photo of pink jellyfish in pale water"></div><div class="meta"><span><svg><use href="#icon-clock"/></svg>5m</span><span><svg><use href="#icon-heart"/></svg>0</span><span><svg><use href="#icon-bubble"/></svg>31</span></div></article>
      <article class="post"><div class="label">Location, other info</div><div class="media media--nebula" role="img" aria-label="Photo of a colourful star nebula"></div><div class="meta"><span><svg><use href="#icon-clock"/></svg>5m</span><span><svg><use href="#icon-heart"/></svg>0</span><span><svg><use href="#icon-bubble"/></svg>31</span></div></article>
      <article class="post"><div class="label">Location</div><div class="media media--tulips" role="img" aria-label="Photo of a red tulip field with one white tulip"></div><div class="meta"><span><svg><use href="#icon-clock"/></svg>5m</span><span><svg><use href="#icon-heart"/></svg>0</span><span><svg><use href="#icon-bubble"/></svg>31</span></div></article>
      <article class="post"><div class="label">Location, other info</div><div class="media media--night" role="img" aria-label="Painting of a night river with glowing reflections"></div><div class="meta"><span><svg><use href="#icon-clock"/></svg>5m</span><span><svg><use href="#icon-heart"/></svg>0</span><span><svg><use href="#icon-bubble"/></svg>31</span></div></article>
    </div>
    <footer class="composer"><svg><use href="#icon-say"/></svg>Say something</footer>
  </section>

</main>
</body>
</html>
```